banner ad

We're looking for a banner similar to the one shown on the attached file. The same 4 keywords, the same text up top, but with new formatting, design and perhaps color scheme. Looking for something to catch people's attention that will stand out on this particular page shown in the attached image. Our goal is to find a banner with a better click through rate than the current version.

```html
<!DOCTYPE html>
<html lang="en">
<head>
<meta charset="utf-8">
<title>Ads Related to Blood Glucose</title>
<link rel="stylesheet" href="https://fonts.googleapis.com/css2?family=Montserrat:wght@800&family=Open+Sans:wght@600&display=swap">
<style>
  :root {
    --navy: #0f2a4a;
    --navy-deep: #0a1f38;
    --coral: #ff6b4a;
    --coral-dark: #e5522f;
    --white: #ffffff;
    --ink: #0f2a4a;
    --photo-family-a: #b9a894;
    --photo-family-b: #6f9cc4;
    --photo-hand-a: #e3bfa8;
    --photo-hand-b: #c9d6df;
  }
  html, body {
    margin: 0;
    padding: 0;
    overflow: hidden;
    background: var(--white);
  }
  .banner {
    position: relative;
    width: 1200px;
    height: 275px;
    overflow: hidden;
    background: radial-gradient(circle at 55% 40%, var(--navy) 0%, var(--navy-deep) 100%);
  }
  .photo-family {
    position: absolute;
    left: 0; top: 0;
    width: 330px; height: 275px;
    background: linear-gradient(120deg, var(--photo-family-a) 0%, var(--photo-family-b) 100%);
    clip-path: polygon(0 0, 100% 0, 85% 100%, 0 100%);
  }
  .photo-hand {
    position: absolute;
    left: 1000px; top: 0;
    width: 200px; height: 275px;
    background: linear-gradient(240deg, var(--photo-hand-a) 0%, var(--photo-hand-b) 100%);
    clip-path: polygon(15% 0, 100% 0, 100% 100%, 0 100%);
  }
  .accent-edge {
    position: absolute;
    left: 0; bottom: 0;
    width: 1200px; height: 8px;
    background: var(--coral);
  }
  .content {
    position: absolute;
    left: 340px; top: 34px;
    width: 650px;
  }
  .heading {
    margin: 0;
    text-align: center;
    font-family: "Montserrat", sans-serif;
    font-weight: 800;
    font-size: 25px;
    letter-spacing: 1.5px;
    line-height: 32px;
    color: var(--white);
  }
  .heading-bar {
    width: 70px;
    height: 4px;
    margin: 10px auto 0;
    border-radius: 2px;
    background: var(--coral);
  }
  .keywords {
    display: grid;
    grid-template-columns: 290px 346px;
    gap: 14px;
    margin-top: 22px;
  }
  .keyword {
    display: flex;
    align-items: center;
    gap: 10px;
    height: 52px;
    padding: 0 12px;
    box-sizing: border-box;
    border-radius: 26px;
    background: var(--white);
    font-family: "Open Sans", sans-serif;
    font-weight: 600;
    font-size: 16px;
    color: var(--ink);
    text-decoration: none;
    white-space: nowrap;
    box-shadow: 0 4px 0 var(--coral-dark);
  }
  .keyword-icon {
    flex: none;
    width: 28px;
    height: 28px;
  }
</style>
</head>
<body>
<div class="banner">
  <div class="photo-family" role="img" aria-label="Smiling grandfather, mother and child sitting together on a sofa"></div>
  <div class="photo-hand" role="img" aria-label="Fingertip being tested with a blood glucose meter"></div>

  <div class="content">
    <h2 class="heading">ADS RELATED TO BLOOD GLUCOSE</h2>
    <div class="heading-bar"></div>

    <nav class="keywords">
      <a class="keyword" href="#">
        <svg class="keyword-icon" viewBox="0 0 28 28" aria-hidden="true"><circle cx="14" cy="14" r="14" fill="var(--coral)"/><path d="M11,8 L18,14 L11,20" fill="none" stroke="var(--white)" stroke-width="3" stroke-linecap="round" stroke-linejoin="round"/></svg>
        <span>Blood Sugars Level chart</span>
      </a>
      <a class="keyword" href="#">
        <svg class="keyword-icon" viewBox="0 0 28 28" aria-hidden="true"><circle cx="14" cy="14" r="14" fill="var(--coral)"/><path d="M11,8 L18,14 L11,20" fill="none" stroke="var(--white)" stroke-width="3" stroke-linecap="round" stroke-linejoin="round"/></svg>
        <span>Normal Blood Sugar Range</span>
      </a>
      <a class="keyword" href="#">
        <svg class="keyword-icon" viewBox="0 0 28 28" aria-hidden="true"><circle cx="14" cy="14" r="14" fill="var(--coral)"/><path d="M11,8 L18,14 L11,20" fill="none" stroke="var(--white)" stroke-width="3" stroke-linecap="round" stroke-linejoin="round"/></svg>
        <span>Blood Glucose</span>
      </a>
      <a class="keyword" href="#">
        <svg class="keyword-icon" viewBox="0 0 28 28" aria-hidden="true"><circle cx="14" cy="14" r="14" fill="var(--coral)"/><path d="M11,8 L18,14 L11,20" fill="none" stroke="var(--white)" stroke-width="3" stroke-linecap="round" stroke-linejoin="round"/></svg>
        <span>What is normal Blood Sugar range</span>
      </a>
    </nav>
  </div>

  <div class="accent-edge"></div>
</div>
</body>
</html>
```